Electronics Recycling and IT Asset Disposition Flyer and Brochure Design

We need a 2 side A5 Flyer and 4 side A4 folder( brochure) for our electronics waste recycling and IT asset management and disposition business.
Our business provides free electronics waste recycling for companies, schools, learning institutions,councils, IT companies and government sectors. Many people are ignorant of responsible recycling of electronics which could harm our health if not treated properly.
The list of other services attached in the pdf.
We provide an end to end and tailored solution for our customers from collection, logistics, data sanitisation, remarketing and recycling.

The Flyer should create awareness of responsible electronics recycling and drive the audience to contact us or go to our website to learn more about the company and services.A brief list of services should also be included in the flyer.The goal is to get the audience to contact us to enquire more about our services.

The Brochure should include all the above plus provide more details about the company, processes, services,contact details (fb, linkedin,Twitter). The goal is to convert the audience to customers for recycling and provide other services as added services.

The final design for both flyer and brochure should communicate responsible recycling of electronic scrap and tailored solution for every organisation.

The company website is www.kelvora-scrap.com.au based in Australia. We serve clients nationwide.

Target Market(s)

IT companies, Corporate, schools and learning institutions, government sector

Industry/Entity Type

Recycling

Contact Information for Business Card

Name: Darren Okefield
email: darren@kelvora-scrap.com.au
website: www.kelvora-scrap.com.au
mobile: +614 173 60294
Phone: 1300 46 2587

Font styles to use
Serif

Requirements
Must have
• I would like the designs to have more images and icons
Nice to have
Should not have
• none

```html
<!DOCTYPE html>
<html lang="en">
<head>
<meta charset="utf-8">
<title>Kelvora Scrap – Brochure Spread</title>
<link href="https://fonts.googleapis.com/css2?family=Jost:wght@400;500;600&display=swap" rel="stylesheet">
<style>
  :root{
    --green:#4d9a3e;
    --green-light:#7cbf5a;
    --green-pale:#a9d68a;
    --ink:#1e1e1e;
    --body:#3a3a3a;
    --muted:#6d6d6d;
    --paper:#f4f5f6;
    --backdrop:#e4e6e8;
  }
  *{box-sizing:border-box;margin:0;padding:0}
  html,body{width:1200px;height:789px;overflow:hidden;background:var(--backdrop)}
  body{font-family:"Jost",Futura,sans-serif;color:var(--body)}
  .spread{position:absolute;left:70px;top:20px;width:1059px;height:749px;display:flex;box-shadow:0 10px 30px rgba(0,0,0,.18)}
  .page{position:relative;width:529.5px;height:749px;background:var(--paper);overflow:hidden}
  .page--left{box-shadow:inset -14px 0 18px -14px rgba(0,0,0,.18)}
  .page--right{box-shadow:inset 14px 0 18px -14px rgba(0,0,0,.18)}
  .page-art{position:absolute;inset:0;width:100%;height:100%}
  .accent-bar{position:absolute;width:62px;height:5px;background:var(--green)}
  .page-title{position:absolute;font-weight:500;font-size:28px;letter-spacing:.5px;color:var(--ink);text-transform:uppercase;line-height:1}
  .service-block{position:absolute;left:40px;top:350px;width:410px}
  .service-block h3,.service-list h3{color:var(--green);font-weight:500;font-size:14.5px;line-height:1.25;margin-top:7px}
  .ticks{list-style:none}
  .ticks li{position:relative;padding-left:16px;font-size:10.6px;line-height:1.35;color:var(--body)}
  .ticks li::before{content:"✓";position:absolute;left:2px;top:0;color:var(--green);font-weight:600}
  .sub-points{font-size:10.6px;line-height:1.35;padding-left:26px}
  .about{position:absolute;left:20px;top:76px;width:488px}
  .about p{font-size:9.8px;line-height:1.4;margin-bottom:8px;color:var(--body)}
  .service-list{position:absolute;left:20px;top:318px;width:488px}
  .service-list h3{font-size:13.5px}
  .facts{position:absolute;left:20px;top:600px;width:440px}
  .facts h2{font-weight:500;font-size:19px;color:var(--ink);text-transform:uppercase;margin-bottom:6px}
  .fact-row{display:flex;justify-content:space-between}
  .fact{width:95px}
  .fact strong{display:block;color:var(--green);font-weight:600;font-size:12px}
  .fact span{display:block;font-size:7.6px;line-height:1.2;color:var(--muted);text-transform:uppercase}
</style>
</head>
<body>
<main class="spread">

  <section class="page page--left">
    <svg class="page-art" viewBox="0 0 529.5 749" aria-hidden="false">
      <defs>
        <linearGradient id="scrapTones" x1="0" y1="0" x2="1" y2="1">
          <stop offset="0" stop-color="#3d5a3a"/>
          <stop offset=".45" stop-color="#6b7f5e"/>
          <stop offset="1" stop-color="#2f3b34"/>
        </linearGradient>
        <linearGradient id="binTones" x1="0" y1="0" x2="0" y2="1">
          <stop offset="0" stop-color="#6a6a6a"/>
          <stop offset="1" stop-color="#cfe08f"/>
        </linearGradient>
      </defs>
      <polygon points="0,0 529.5,0 529.5,190 0,290" fill="url(#scrapTones)" role="img" aria-label="Photograph of a pile of discarded circuit boards and electronic parts"/>
      <polygon points="300,240 529.5,192 529.5,330" fill="var(--green)"/>
      <g transform="translate(478,246)" fill="none" stroke="#fff" stroke-width="5" stroke-linecap="round">
        <path d="M-14,8 A16,16 0 0 1 -6,-14"/>
        <path d="M4,-15 A16,16 0 0 1 16,4"/>
        <path d="M10,13 A16,16 0 0 1 -12,12"/>
        <g fill="#fff" stroke="none">
          <polygon points="-10,-18 0,-14 -8,-6"/>
          <polygon points="20,-2 16,10 10,2"/>
          <polygon points="-6,18 -18,14 -10,6"/>
        </g>
      </g>
      <polygon points="260,749 529.5,590 529.5,749" fill="var(--green-light)"/>
      <rect x="355" y="520" width="130" height="175" rx="8" fill="url(#binTones)" role="img" aria-label="Illustration of a recycling bin filled with old electronic devices"/>
    </svg>

    <div class="accent-bar" style="left:40px;top:302px"></div>
    <h1 class="page-title" style="left:40px;top:314px">Service Offering</h1>

    <div class="service-block">
      <h3>Secure E-Waste Collection Service</h3>
      <ul class="ticks">
        <li>Kelvora Scrap collects electronic waste from schools, businesses, home users and government departments</li>
        <li>Secure collection includes pick up of e-waste and transportation to our recycling facility in a secured truck</li>
        <li>Registration of assets and reporting</li>
      </ul>
      <h3>Receipting Registration, Test and Audit Services</h3>
      <ul class="ticks">
        <li>Registering your assets on our Asset Management System</li>
        <li>Test, audit and verify specifications, condition and resale value</li>
        <li>Provide a detailed asset report</li>
        <li>Cleaning and removal of company logos and asset tags</li>
      </ul>
      <h3>Certified Data Erasure Services</h3>
      <ul class="ticks">
        <li>To provide secure data destruction:</li>
      </ul>
      <div class="sub-points">•X1 pass<br>•X3 pass (Recommended, DoD standard)<br>•X7 pass</div>
      <ul class="ticks">
        <li>Total destruction of HDDs by degaussing</li>
        <li>Total physical destruction of any storage media by shredding</li>
      </ul>
    </div>
  </section>

  <section class="page page--right">
    <svg class="page-art" viewBox="0 0 529.5 749">
      <defs>
        <linearGradient id="officeTones" x1="0" y1="0" x2="1" y2="0">
          <stop offset="0" stop-color="#f4f5f6" stop-opacity="0"/>
          <stop offset=".5" stop-color="#dfe2e4"/>
          <stop offset="1" stop-color="#cdd1d4"/>
        </linearGradient>
      </defs>
      <rect x="0" y="0" width="529.5" height="300" fill="url(#officeTones)" opacity=".7" role="img" aria-label="Faint photograph of an engineer at work in an office"/>
      <polygon points="340,749 529.5,610 529.5,749" fill="var(--green-light)"/>
      <polygon points="380,749 529.5,640 529.5,749" fill="var(--paper)" opacity=".0"/>
    </svg>

    <div class="accent-bar" style="left:20px;top:24px"></div>
    <h1 class="page-title" style="left:20px;top:36px;font-size:26px">Who We Are</h1>

    <div class="about">
      <p>Kelvora Scrap is a full service IT asset disposition, electronics waste recycling and electronics scrap purchasing company in Australia. Our vision is to become an industry leader by building genuine relationships with clients based on integrity, service quality and consistency, as well as maximizing value recovery.</p>
      <p>Our focus is to reduce electronic waste generation through creating awareness in organisations and community about the importance of responsible recycling of electronics waste. Our goal is to provide end-to-end solution in e-waste management through established processes and technological innovations, drive higher returns for our customers and enhance conservation of raw metals within our ecosystem.</p>
      <p>Our team of dedicated engineers and professionals work with companies, government offices, institutions and SMEs across Australia to provide personalised IT asset disposal and e-waste management solutions to suit their needs. Our experience and knowledge in this industry will help us to understand and provide innovative solutions to manage your end of life IT assets. We aim at maximising returns and providing cost effective ways to ensure a positive impact on your bottom-line.</p>
    </div>

    <div class="service-list">
      <h3>IT Asset Remarketing</h3>
      <ul class="ticks"><li>Recover client's IT asset and mobile devices for valuation and remarketing</li></ul>
      <h3>Processing &amp; recycling of electronic waste</h3>
      <ul class="ticks"><li>All assets with no market value will be processed as E-Waste and recycled with zero to landfill in our ISO certified partner refinery overseas for metals recovery</li></ul>
      <h3>IT Services&amp; Data CenterSetup, Relocation and Decommissioning</h3>
      <ul class="ticks">
        <li>Deployment, relocation and decommissioning of IT systems by professional Veranto and Norlink certified engineers</li>
        <li>Data Center decommissioning/racking/de-racking and relocation</li>
        <li>IT Systems deployment and support for small and medium size business</li>
      </ul>
      <h3>IT Asset Auditing</h3>
      <ul class="ticks"><li>Recording of Manufacturer and Model per asset (additionally HDD quantity and capacity for Server &amp; Storage assets)</li></ul>
    </div>

    <div class="facts">
      <h2>Facts</h2>
      <div class="fact-row">
        <div class="fact"><strong>8 bil</strong><span>Connected devices globally</span></div>
        <div class="fact"><strong>110%</strong><span>Mobile broadband penetration in Australia</span></div>
        <div class="fact"><strong>33%</strong><span>World's ewaste growth by 2017</span></div>
        <div class="fact"><strong>2 bil</strong><span>Pcs worldwide</span></div>
      </div>
    </div>
  </section>

</main>
</body>
</html>
```